Halt and Thicken New Branding Stationary Set - updated Oct 30th 2017

Updated on 30th Oct 2017 as we now need a whole folder design instead of a folder cover. We have thought out exactly what should be on it so it wont be hard. We are happy for this to be completed only by the winning designer if you like. And also we are guaranteeing this project now. Thanks!

We just got our new logo and now we would like a stationary set so we can brand our company communications. The items we need designed are:
Business cards
Letterhead
Appointment confirmation cards
Folder - switched from folder cover. Note that if you don't wish to do this unless you are selected as the winner this is fine.

1. Business cards - for 5 employees, final names will be given once the winner is selected, but you can use this one as the sample:
Lucinda Prieto
Hair Regrowth Expert
Halt and Thicken
7127 Marbury Ave, Suite 500
Kestrel Park CA 90877
lucinda@gavinthorpemd.example
(555) 238-9016

2. Letterhead 8.5" x 11.0" vertical
Halt and Thicken
Kestrel Park CA 90877
office@haltandthicken.example
(555) 238-9016

3. Appointment Confirmation cards - business card size
Halt and Thicken
Kestrel Park CA 90877
Appointment For:
Date:
Time:
If you are unable to make your appointment, please contact us to reschedule at:
(555) 238-9016
info@gavinthorpemd.example

*UPDATED*
4. Folder 9" x 12 " vertical with double pocket
We would like the infinity image from the logo made really big so the left side is on the back and the right side with the + sign is on the front and its takes up the maximum room on the folder.
On the front below the half logo it should say "A Biochemical Revolution..."
On the inside we would also like to have the infinity sign from the logo but faded and half on the left pocket half on the right.
On left inside pocket it should say (this will be partically written on top of the logo):
Gavin Thorpe MD
Precision Medicine
Halt and Thicken Hair
On the Right inside pocket it should say the following:
Because the Enemy of BETTER Health is Good Health
BETTER Ingredients
BETTER Recipe
BETTER Medicine
On the back below the logo on the bottom should be the contact information.
I attached a picture of our drawing of what we want for this to make it easier.

Here is our website to give you an idea of our branding: http://www.haltandthicken.example/

We are the only true cure for hair loss and need to look professional and highest quality and beyond reproach from an ethical standpoint. We are a medical clinic so this should be portrayed also.
We cured hair loss by analyzing biochemistry and rebalancing it so that the process reverses and your own hair can grow back naturally.

Business card information:

OK so here is the information for the business cards:

Lucinda Prieto
Hair Regrowth Expert
(555) 238-9016
www.haltandthicken.example

Marisol Quintero
Hair Growth Consultant
(555) 238-9016
marisol@gavinthorpemd.example
www.haltandthicken.example

Glenda Hutchins
CMO/COO
(555) 238-9016
glenda@haltandthicken.example
www.haltandthicken.example

Dr Lou Thorpe
President
(555) 238-9016
info@gavinthorpemd.example
www.haltandthicken.example

Halt and Thicken
Customer Service
(555) 238-9016
info@gavinthorpemd.example
www.haltandthicken.example

Target Market(s)

Men aged 20-24 who care about their appearance, care about their hair and care about the world.

Industry/Entity Type

Medical And Science

Font styles to use
Sans Serif

Colors
00a990
ffffff
9d9d9d
333333

Requirements
Must have
• Must use the logo and our brand colors from the logo in all designs.
• The pantone colors are:
• Green: #4ca26f
• Light Grey: #999999
• The design should be symmetrical and balanced.
Nice to have
• It should look reasonably masculine.
Should not have
• Do not include any red in the design.

```html
<!DOCTYPE html>
<html lang="en">
<head>
<meta charset="utf-8">
<title>Halt and Thicken – Business Card</title>
<link rel="stylesheet" href="https://fonts.googleapis.com/css2?family=Open+Sans:wght@300;400;600;700&display=swap">
<style>
  :root {
    --green: #4ca26f;
    --green-deep: #1f6e42;
    --green-light: #8fd3ac;
    --grey: #999999;
    --grey-light: #e4e4e4;
    --text: #555555;
    --white: #ffffff;
    --backdrop: #e9ecea;
  }
  * { box-sizing: border-box; margin: 0; padding: 0; }
  html, body { width: 1200px; height: 856px; overflow: hidden; }
  body {
    background: var(--backdrop);
    font-family: "Open Sans", Arial, sans-serif;
    position: relative;
  }
  .card {
    position: absolute;
    width: 520px;
    height: 297px;
    border-radius: 26px;
    overflow: hidden;
    box-shadow: 0 6px 18px rgba(0,0,0,.12);
  }
  .card--front { left: 50px; top: 280px; background: var(--white); }
  .card--back  { left: 630px; top: 280px; }
  .card__art { position: absolute; inset: 0; width: 100%; height: 100%; }

  .brand { position: absolute; display: flex; align-items: center; gap: 8px; font-weight: 700; letter-spacing: .3px; }
  .brand__dot { width: 16px; height: 16px; border-radius: 50%; }
  .card--front .brand { left: 160px; top: 44px; color: var(--green); font-size: 21px; }
  .card--front .brand__dot { background: var(--green); }
  .card--back .brand { left: 240px; top: 66px; color: var(--white); font-size: 26px; }
  .card--back .brand__dot { background: var(--white); width: 20px; height: 20px; }

  .contact { position: absolute; left: 238px; top: 104px; list-style: none; color: var(--text); font-size: 12.5px; line-height: 1.45; }
  .contact li { display: flex; align-items: flex-start; gap: 8px; margin-bottom: 3px; }
  .contact svg { flex: none; width: 15px; height: 15px; margin-top: 2px; }

  .person { position: absolute; left: 34px; bottom: 28px; color: var(--white); }
  .person__name { font-size: 20px; font-weight: 700; }
  .person__role { font-size: 11px; font-weight: 300; letter-spacing: 1px; text-transform: uppercase; }

  .website { position: absolute; left: 30px; bottom: 26px; color: var(--white); font-size: 13px; font-weight: 600; }
</style>
</head>
<body>

<section class="card card--front" aria-label="Business card front">
  <svg class="card__art" viewBox="0 0 520 297" preserveAspectRatio="none" aria-hidden="true">
    <defs>
      <linearGradient id="frontGreen" x1="0" y1="0" x2="0.4" y2="1">
        <stop offset="0" stop-color="#4ca26f"/>
        <stop offset="1" stop-color="#1f6e42"/>
      </linearGradient>
      <linearGradient id="frontGrey" x1="0" y1="0" x2="1" y2="1">
        <stop offset="0" stop-color="#efefef"/>
        <stop offset="1" stop-color="#b5b5b5"/>
      </linearGradient>
    </defs>
    <path d="M290,0 C400,8 480,45 520,110 L520,0 Z" fill="url(#frontGreen)"/>
    <path d="M70,0 L125,0 C190,110 330,195 520,232 L520,246 C300,222 120,150 0,22 L0,0 Z" fill="url(#frontGrey)"/>
    <path d="M0,34 C120,160 290,235 520,252 L520,297 L0,297 Z" fill="url(#frontGreen)"/>
    <path d="M0,28 C120,155 290,230 520,247" fill="none" stroke="#ffffff" stroke-width="5"/>
  </svg>

  <div class="brand"><span class="brand__dot"></span>Halt and Thicken</div>

  <ul class="contact">
    <li>
      <svg viewBox="0 0 16 16"><circle cx="8" cy="8" r="8" fill="var(--green)"/><path d="M8 3.5a3 3 0 0 0-3 3c0 2.2 3 5.8 3 5.8s3-3.6 3-5.8a3 3 0 0 0-3-3z" fill="#fff"/><circle cx="8" cy="6.5" r="1.1" fill="var(--green)"/></svg>
      <span>7127 Marbury Ave, Suite 500<br>Kestrel Park CA 90877</span>
    </li>
    <li>
      <svg viewBox="0 0 16 16"><circle cx="8" cy="8" r="8" fill="var(--green)"/><path d="M5 5.5h6l1 2.5H4z M5.5 8.5h5v3h-5z" fill="#fff"/></svg>
      <span>(555) 238-9016</span>
    </li>
    <li>
      <svg viewBox="0 0 16 16"><circle cx="8" cy="8" r="8" fill="var(--green)"/><rect x="4" y="5.2" width="8" height="5.6" fill="#fff"/><path d="M4 5.2l4 3 4-3" fill="none" stroke="var(--green)" stroke-width="0.9"/></svg>
      <span>office@haltandthicken.example</span>
    </li>
  </ul>

  <div class="person">
    <p class="person__name">Example Name</p>
    <p class="person__role">President</p>
  </div>
</section>

<section class="card card--back" aria-label="Business card back">
  <svg class="card__art" viewBox="0 0 520 297" preserveAspectRatio="none" aria-hidden="true">
    <defs>
      <linearGradient id="backGreen" x1="0.2" y1="0" x2="0.6" y2="1">
        <stop offset="0" stop-color="#8fd3ac"/>
        <stop offset="0.35" stop-color="#4ca26f"/>
        <stop offset="1" stop-color="#1f6e42"/>
      </linearGradient>
      <linearGradient id="backGrey" x1="0" y1="0" x2="0.3" y2="1">
        <stop offset="0" stop-color="#e6e6e6"/>
        <stop offset="1" stop-color="#8f8f8f"/>
      </linearGradient>
    </defs>
    <rect width="520" height="297" fill="url(#backGreen)"/>
    <path d="M0,0 L90,0 C170,110 320,195 520,228 L520,297 L0,297 Z" fill="url(#backGrey)"/>
    <path d="M0,14 C140,60 290,170 450,225" fill="none" stroke="#4ca26f" stroke-width="6"/>
    <path d="M90,0 C170,110 320,195 520,228" fill="none" stroke="#ffffff" stroke-opacity=".6" stroke-width="2"/>
  </svg>

  <div class="brand"><span class="brand__dot"></span>Halt and Thicken</div>
  <p class="website">www.haltandthicken.example</p>
</section>

</body>
</html>
```